VENTIX Business Card

VENTIX (www.ventixpools.example) is a veteran in the swimming pool maintenance and repair business..we have served our clients for 15 years and have a research chemist, an electrician, a plumber and a pool building contractor (in part) on staff...We want to provide a business card that has a dual purpose, that people want to keep around, that leaves people speechless in the sense that they understand the mission of and the experience level of the TEAM at VENTIX.

Target Market(s)

persons who enjoy swimming and make it a priority to swim

Industry/Entity Type

Building

Font styles to use
Serif
Sans Serif

Colors
85acd3
3176b5
95b6d8
3276b5
0355a3
0555a3
0255a3
0455a3
85abd2

Requirements
Must have
• name, title, address, email, text
Nice to have
• a die cut shape
Should not have
• cartoons, pictures of pools

```html
<!DOCTYPE html>
<html lang="en">
<head>
<meta charset="utf-8">
<title>VENTIX Business Card</title>
<link href="https://fonts.googleapis.com/css2?family=Open+Sans:wght@400;600;700&family=Jost:wght@400&display=swap" rel="stylesheet">
<style>
  :root {
    --bg: #dcdde0;
    --brand-blue: #338cb0;
    --brand-deep: #2f86ab;
    --brand-light: #4bb0dc;
    --ink: #2b2b2b;
    --paper: #ffffff;
  }
  * { margin: 0; padding: 0; box-sizing: border-box; }
  html, body { width: 1200px; height: 800px; overflow: hidden; }
  body {
    background: var(--bg);
    font-family: "Open Sans", Arial, sans-serif;
    position: relative;
  }
  .card {
    position: absolute;
    top: 250px;
    width: 525px;
    height: 300px;
    box-shadow: 0 6px 18px rgba(0,0,0,0.12);
    overflow: hidden;
  }
  .card-front { left: 50px; background: var(--brand-blue); }
  .card-back { left: 625px; background: var(--paper); }

  .front-brand {
    position: absolute;
    left: 0; right: 0; top: 98px;
    text-align: center;
    color: var(--paper);
  }
  .brand-name {
    font-family: "Open Sans", Arial, sans-serif;
    font-weight: 600;
    font-size: 62px;
    line-height: 1;
    letter-spacing: 2px;
  }
  .tagline {
    font-family: "Jost", "Futura", sans-serif;
    font-size: 15px;
    letter-spacing: 3px;
    margin-top: 12px;
  }

  .contact {
    position: absolute;
    left: 40px; top: 40px;
    color: var(--ink);
    font-size: 13px;
    line-height: 1.4;
  }
  .person-name { color: var(--brand-deep); font-weight: 700; font-size: 17px; line-height: 1.2; }
  .person-title { font-size: 13px; margin-bottom: 14px; }
  .contact-line { display: flex; align-items: center; gap: 7px; }
  .contact-line svg { width: 11px; height: 11px; fill: var(--brand-deep); flex: none; }
  .address { margin-bottom: 2px; }

  .back-brand {
    position: absolute;
    right: 38px; top: 92px;
    text-align: center;
    color: var(--brand-deep);
  }
  .back-brand .brand-name { font-size: 48px; }
  .back-brand .tagline { color: var(--brand-light); font-size: 12px; letter-spacing: 2px; margin-top: 8px; }

  .website {
    position: absolute;
    right: 40px; bottom: 42px;
    font-size: 13px;
    color: var(--ink);
  }
  .stripe {
    position: absolute;
    left: 0; right: 0; bottom: 0;
    height: 18px;
    background: var(--brand-deep);
  }
  .stripe-accent {
    position: absolute;
    left: 315px; width: 150px; height: 100%;
    background: var(--brand-light);
  }
</style>
</head>
<body>
  <section class="card card-front" aria-label="Card front">
    <div class="front-brand">
      <div class="brand-name">VENTIX</div>
      <div class="tagline">POOL CARE...DONE RIGHT</div>
    </div>
  </section>

  <section class="card card-back" aria-label="Card back">
    <div class="contact">
      <div class="person-name">Alex Marlow</div>
      <div class="person-title">Consultant</div>
      <div class="address">42 Harbor Lane<br>Lakeview, QZ, 20000</div>
      <div class="contact-line">
        <svg viewBox="0 0 24 24" aria-hidden="true"><path d="M6.6 10.8a15.1 15.1 0 0 0 6.6 6.6l2.2-2.2a1 1 0 0 1 1-.25 11.4 11.4 0 0 0 3.6.57 1 1 0 0 1 1 1V20a1 1 0 0 1-1 1A17 17 0 0 1 3 4a1 1 0 0 1 1-1h3.5a1 1 0 0 1 1 1c0 1.25.2 2.45.57 3.57a1 1 0 0 1-.25 1z"/></svg>
        <span>555-010-2468</span>
      </div>
      <div class="contact-line">
        <svg viewBox="0 0 24 24" aria-hidden="true"><path d="M6 2h12v5H6zM4 8h16a2 2 0 0 1 2 2v7h-4v5H6v-5H2v-7a2 2 0 0 1 2-2zm4 8v4h8v-4z"/></svg>
        <span>555-010-1357</span>
      </div>
      <div class="contact-line">
        <svg viewBox="0 0 24 24" aria-hidden="true"><path d="M2 5h20v14H2zm2 2v.5l8 5 8-5V7z"/></svg>
        <span>alex@ventixpools.example</span>
      </div>
    </div>

    <div class="back-brand">
      <div class="brand-name">VENTIX</div>
      <div class="tagline">POOL CARE...DONE RIGHT</div>
    </div>

    <div class="website">www.ventixpools.example</div>
    <div class="stripe"><div class="stripe-accent"></div></div>
  </section>
</body>
</html>
```